普段のお店は入りづらい雰囲気になっています。一部の時間のみ、色々な方が入りやすいような雰囲気を作るために目立つのぼりを立てたいです

BARとしてのお店のイメージもありますので、居酒屋さんのようなのぼりではなく、Barらしさが出ていると良いなと思います。

ハッピーアワーの文字が一番目立つように(カタカナ、英語どちらでも)。時間も載せたいところですが、変更するかもしれないので今回は載せなくて構いません。店名とロゴ、ビールは瓶ビールなので、瓶ビールやワイン、カクテル(ロングカクテル)などのイラスト等と、カクテル¥500 ウイスキー半額というフレーズを載せて頂きたいです。

色味は指定していますが、白黒グレー系でも目立つ感じであれば構いません。
一目でわかりやすいものを希望します。

メニュー等の詳細は別で看板を出す予定でいます。
店名 ORVA

シンプル 複雑
単色 カラフル
暗い 明るい
日常 高級
遊び心 厳粛
未来的 伝統的
女性的 男性的
赤系、黄・オレンジ系、茶系
のぼり自体はミトネオに入稿して注文する予定です。
レギュラーサイズの左側・縦 1800×600

以前こちらでお願いした際に、データファイルのやり取りで時間をとられたことがあります。なのでミトネオに簡単にデータ入稿出来るものを頂きたいです。

素人ですので、その辺了承して下さる方にお願いしたいと思います。
(とはいえ、最低限普通の事は分かりますので大丈夫です)

のぼりを置く場所も添付します。ビルの入り口付近(同じような雰囲気で2方向あります)に何個かずつ立てる予定でいます。
ご希望がありましたので、aiのロゴデータを追加します
載せて頂きたい文言につきましては、選ばせて頂いた方に内容の変更をお願いするかと思います。
よろしくお願い致します。

男女ともに入りやすいイメージを持っていただけるのでは、と思いました。
お酒の画像もパッと見た感じ分かりやすく、カジュアル感、Barらしさも出ていてよかったです。

たくさんの方から応募を頂き、スタッフの意見も聞きつつ、悩んだ上で一つを選ばせて頂きました。
お店の事を色々な方に一緒に考えて頂き有り難かったです。
また今後もお世話になると思いますので、その際にはよろしくお願い致します。
ありがとうございました。

```html
<!DOCTYPE html>
<html lang="ja">
<head>
<meta charset="UTF-8">
<title>ORVA ハッピーアワー のぼり</title>
<link rel="stylesheet" href="https://fonts.googleapis.com/css2?family=Noto+Serif+JP:wght@500;700;900&family=Marcellus&family=Playfair+Display:wght@700&display=swap">
<style>
  :root {
    --paper: #ffffff;
    --banner-dark: #231815;
    --accent-yellow: #fff200;
    --accent-orange: #f39800;
    --gold-light: #fff3c4;
    --gold-mid: #d9b45a;
    --gold-deep: #9a7420;
    --logo-gray: #8c8c8c;
    --loop-edge: #9a9a9a;
    --text-white: #ffffff;
  }
  html, body {
    margin: 0;
    padding: 0;
    width: 1200px;
    height: 2860px;
    overflow: hidden;
    background: var(--paper);
  }
  .canvas {
    position: relative;
    width: 1200px;
    height: 2860px;
    background: var(--paper);
    overflow: hidden;
  }
  .pole-loop {
    position: absolute;
    left: 100px;
    width: 84px;
    height: 40px;
    background: var(--paper);
    border: 3px solid var(--loop-edge);
    box-sizing: border-box;
  }
  .banner {
    position: absolute;
    left: 150px;
    top: 112px;
    width: 900px;
    height: 2648px;
    background: var(--banner-dark);
    overflow: hidden;
  }
  .banner-base {
    position: absolute;
    left: 0;
    top: 1800px;
    width: 900px;
    height: 848px;
  }
  .headline-en {
    position: absolute;
    top: 100px;
    left: 0;
    width: 900px;
    text-align: center;
    font-family: "Playfair Display", "Noto Serif JP", serif;
    font-weight: 700;
    font-size: 92px;
    letter-spacing: 2px;
    color: var(--text-white);
    margin: 0;
  }
  .now-badge {
    position: absolute;
    left: 202px;
    top: 308px;
    width: 200px;
    height: 200px;
    border-radius: 50%;
    background: var(--accent-orange);
    color: var(--text-white);
    font-family: "Noto Serif JP", serif;
    font-weight: 900;
    font-size: 76px;
    display: flex;
    align-items: center;
    justify-content: center;
  }
  .gold-type {
    position: absolute;
    writing-mode: vertical-rl;
    font-family: "Noto Serif JP", serif;
    font-weight: 900;
    background: linear-gradient(180deg, var(--gold-light) 0%, var(--gold-mid) 35%, var(--gold-deep) 55%, var(--gold-light) 75%, var(--gold-mid) 100%);
    -webkit-background-clip: text;
    background-clip: text;
    color: transparent;
    margin: 0;
    line-height: 1;
  }
  .headline-ja {
    left: 520px;
    top: 300px;
    font-size: 218px;
    letter-spacing: -6px;
  }
  .status {
    left: 212px;
    top: 540px;
    font-size: 186px;
    letter-spacing: 4px;
  }
  .offer-list {
    position: absolute;
    left: 110px;
    top: 1530px;
    margin: 0;
    padding: 0;
    list-style: none;
    font-family: "Noto Serif JP", serif;
    font-weight: 500;
    font-size: 46px;
    line-height: 72px;
    color: var(--text-white);
    letter-spacing: 3px;
  }
  .drinks-illustration {
    position: absolute;
    left: 110px;
    top: 1670px;
    width: 380px;
    height: 160px;
    background: linear-gradient(180deg, #f4f4f4, #dcdcdc);
    border-radius: 14px;
  }
  .logo-square {
    position: absolute;
    left: 360px;
    top: 2010px;
    width: 180px;
    height: 180px;
    background: var(--logo-gray);
  }
  .shop-name {
    position: absolute;
    left: 0;
    top: 2300px;
    width: 900px;
    text-align: center;
    font-family: "Marcellus", "Noto Serif JP", serif;
    color: var(--logo-gray);
    margin: 0;
  }
  .shop-name .shop-type {
    display: block;
    font-size: 30px;
    letter-spacing: 26px;
    padding-left: 26px;
    margin-bottom: 36px;
  }
  .shop-name .shop-word {
    display: block;
    font-size: 150px;
    letter-spacing: 34px;
    padding-left: 34px;
    line-height: 1;
  }
</style>
</head>
<body>
<div class="canvas">
  <div class="pole-loop" style="top:132px"></div>
  <div class="pole-loop" style="top:780px"></div>
  <div class="pole-loop" style="top:1400px"></div>
  <div class="pole-loop" style="top:2040px"></div>
  <div class="pole-loop" style="top:2640px"></div>

  <div class="banner">
    <svg class="banner-base" viewBox="0 0 900 848" aria-hidden="true">
      <path d="M0 150 C 180 150, 260 40, 470 40 C 650 40, 720 110, 900 80 L 900 848 L 0 848 Z" fill="var(--accent-yellow)"/>
    </svg>

    <h1 class="headline-en">HAPPY HOUR</h1>
    <div class="now-badge">只今</div>
    <p class="gold-type status">実施中</p>
    <p class="gold-type headline-ja">ハッピーアワー</p>

    <ul class="offer-list">
      <li>カクテル ¥500</li>
      <li>ウイスキー 半額</li>
    </ul>
    <div class="drinks-illustration" role="img" aria-label="瓶ビール・ワインボトル・カクテルグラス・ウイスキーボトルのイラスト"></div>

    <div class="logo-square"></div>
    <p class="shop-name">
      <span class="shop-type">BAR</span>
      <span class="shop-word">ORVA</span>
    </p>
  </div>
</div>
</body>
</html>
```